Business Card Design Project

The business card is for an educational company that provides personalised tuition to students.

The company logo is in orange and blue (as provided) and should be included in the name card design

The philosophy of the company is to make learning a comfortable experience for student as such design of the namecard should look fresh and has a bit of the 'wow' factor. Some of the namecard design that appeals to me are as uploaded under Sample Design.

The particulars that need to be provided are:
(1): Company Name (Quillmont Education)
(1): Name
(2): Educational qualifications which will appear below name
(3): Mobile number
(4): Email address
(5): Website

Industry/Entity Type

Business

Requirements
Must have
• (1): Company Logo

(2): The card background should preferably be coloured both for the front side and back.

(3): The choice of font is important as part of the selection consideration. There is no preferred font that I have selected, designer is free to choose the font that will complement their design.

```html
<!DOCTYPE html>
<html lang="en">
<head>
<meta charset="utf-8">
<title>Quillmont Education business card</title>
<link rel="stylesheet" href="https://fonts.googleapis.com/css2?family=Michroma&family=Open+Sans:wght@400;600&family=Montserrat:wght@700&display=swap">
<style>
  :root {
    --stage: #4a4d57;
    --card: #17181d;
    --card-glow: #2d3039;
    --ink: #ffffff;
    --logo-ink: #5b5d64;
    --logo-mark: #ef7a22;
  }
  * { margin: 0; padding: 0; box-sizing: border-box; }
  html, body {
    width: 1200px; height: 1000px; overflow: hidden;
    background: var(--stage);
  }
  .canvas { position: relative; width: 1200px; height: 1000px; }
  .card {
    position: absolute; left: 255px; width: 654px; height: 400px;
    background: radial-gradient(circle at 28% 50%, var(--card-glow) 0%, var(--card) 42%, var(--card) 100%);
    box-shadow: 0 4px 10px rgba(0,0,0,.35);
  }
  .card--front { top: 18px; }
  .card--back { top: 453px; }

  .brand {
    position: absolute; display: flex; align-items: center; gap: 10px;
  }
  .card--front .brand { left: 122px; top: 165px; }
  .card--back .brand { left: 117px; top: 160px; }
  .brand__square { width: 60px; height: 60px; border-radius: 6px; background: var(--logo-mark); }
  .brand__name {
    font-family: "Open Sans", sans-serif; font-weight: 400;
    font-size: 25px; line-height: 28px; color: var(--logo-ink);
  }

  .divider { position: absolute; left: 376px; width: 22px; background: var(--ink); }
  .card--front .divider { top: 122px; height: 124px; }
  .card--back .divider { top: 79px; height: 235px; }

  .monogram {
    position: absolute; left: 420px; top: 136px;
    font-family: "Montserrat", sans-serif; font-weight: 700;
    font-size: 110px; line-height: 110px; color: var(--ink); letter-spacing: -4px;
  }

  .company {
    position: absolute; left: 423px; top: 74px;
    font-family: "Michroma", sans-serif; font-size: 22px; line-height: 32px;
    color: var(--ink); font-weight: 400; -webkit-text-stroke: .6px var(--ink);
  }
  .details { position: absolute; left: 415px; top: 164px; list-style: none; }
  .details li {
    font-family: "Open Sans", sans-serif; font-weight: 600; font-size: 11.5px;
    color: var(--ink); position: absolute; left: 0; white-space: nowrap;
  }
</style>
</head>
<body>
<main class="canvas">
  <section class="card card--front" aria-label="Card front">
    <div class="brand">
      <span class="brand__square"></span>
      <span class="brand__name">Quillmont<br>Education</span>
    </div>
    <span class="divider"></span>
    <span class="monogram">QE</span>
  </section>

  <section class="card card--back" aria-label="Card back">
    <div class="brand">
      <span class="brand__square"></span>
      <span class="brand__name">Quillmont<br>Education</span>
    </div>
    <span class="divider"></span>
    <h1 class="company">Quillmont<br>Education</h1>
    <ul class="details">
      <li style="top:0">NAME:</li>
      <li style="top:25px">Educational qualifications:</li>
      <li style="top:78px">mobile number:</li>
      <li style="top:106px">email:</li>
      <li style="top:132px">website:</li>
    </ul>
  </section>
</main>
</body>
</html>
```